Bright Path Attorneys Billboard Design for Personal Injury Law Firm

Need a billboard design that we can use for different versions. 1400px X 400px jpeg or png
I have attached the logo and the attorney for the billboard. Attorney Marla Benning
Here is a link to our current website brightpathlegalgroup.example

HEADLINE: HIT BY A TRUCK?
SUBHEAD: NO FEE. BIG FIGHT.
877-GRANTLY

HEADLINE: ACCIDENT?
SUBHEAD: NO FEE, UNLESS WE WIN!
877-GRANTLY

HEADLINE: BIG TRUCK. BIG CASE.
SUBHEAD: YOU PAY $0 UPFRONT
877-GRANTLY

Target Market(s)

People in Car Accident

Industry/Entity Type

Personal Injury Attorneys

```html
<!DOCTYPE html>
<html lang="en">
<head>
<meta charset="utf-8">
<title>Bright Path Attorneys – Billboard</title>
<link rel="stylesheet" href="https://fonts.googleapis.com/css2?family=Montserrat:wght@600;700;800;900&display=swap">
<style>
  :root{
    --page:#e6e6ea;
    --board-dark:#3c3c3e;
    --stripe-dark:#2e2e30;
    --brand-green:#5fdc45;
    --text-white:#ffffff;
    --text-dark:#3a3a3c;
    --strip-light:#f4f4f4;
    --strip-shade:#dcdcdc;
  }
  *{margin:0;padding:0;box-sizing:border-box}
  html,body{width:1200px;height:756px;overflow:hidden}
  body{background:var(--page);font-family:"Montserrat",sans-serif;position:relative}
  .billboard{
    position:absolute;left:40px;top:218px;width:1120px;height:320px;
    background:var(--board-dark);overflow:hidden;
    box-shadow:0 10px 30px rgba(0,0,0,.18);
  }
  .billboard__shapes{position:absolute;inset:0}
  .headline{
    position:absolute;left:18px;top:-2px;
    font-weight:900;font-size:84px;line-height:1;color:var(--brand-green);
    letter-spacing:-1px;white-space:nowrap;
  }
  .subhead{
    position:absolute;left:20px;top:76px;
    font-weight:900;font-size:58px;line-height:1;color:var(--text-white);
    letter-spacing:-.5px;white-space:nowrap;
  }
  .phone{
    position:absolute;left:18px;top:140px;
    font-weight:900;font-size:82px;line-height:1;color:var(--text-dark);
    letter-spacing:-1px;white-space:nowrap;
  }
  .website{
    position:absolute;left:20px;top:254px;
    font-weight:700;font-size:28px;color:var(--text-dark);white-space:nowrap;
  }
  .brand{
    position:absolute;left:680px;top:252px;display:flex;align-items:center;gap:8px;
  }
  .brand__dot{width:14px;height:14px;border-radius:50%;background:var(--brand-green);flex:none}
  .brand__name{
    font-weight:700;font-size:15px;line-height:1.15;color:var(--text-dark);width:100px;
  }
  .crash-photo{
    position:absolute;right:0;top:72px;width:320px;height:248px;
    background:linear-gradient(160deg,#d9dbde 0%,#b7babf 45%,#f2f2f2 100%);
    clip-path:polygon(6% 18%,30% 0,78% 0,100% 8%,100% 100%,0 100%,0 40%);
  }
</style>
</head>
<body>
  <section class="billboard">
    <svg class="billboard__shapes" width="1120" height="320" viewBox="0 0 1120 320" aria-hidden="true">
      <polygon points="0,148 760,148 800,236 0,236" fill="var(--brand-green)"/>
      <polygon points="772,148 792,148 832,236 812,236" fill="var(--stripe-dark)"/>
      <polygon points="0,236 820,236 820,320 0,320" fill="var(--strip-light)"/>
      <polygon points="640,236 820,236 820,320 612,320" fill="var(--strip-shade)"/>
      <polygon points="640,236 650,236 622,320 612,320" fill="var(--text-dark)"/>
    </svg>

    <h1 class="headline">HIT BY A TRUCK?</h1>
    <p class="subhead">NO FEE. BIG FIGHT.</p>
    <p class="phone">877-GRANTLY</p>
    <p class="website">brightpathlegalgroup.example</p>

    <div class="brand">
      <span class="brand__dot"></span>
      <span class="brand__name">Bright Path Attorneys</span>
    </div>

    <div class="crash-photo" role="img" aria-label="Photo of a white SUV with a crushed front end after a collision"></div>
  </section>
</body>
</html>
```